Memorial page to show case the life and works of an individual who has passed

I would like to design a website as a memorial page for my mother. She was a very senior member of the London community and would like to design something that has a page for her biography. Gallery. Testimonials. Etc. Something that is smart and modern.
similar to
http://www.gervaldquinnstudio.org/
Not to have things that are flowery it need to be a website that is smart clean and proffesional to showcase the life and works of an indiviudal

there wont be a logo as it is not a company

Industry/Entity Type

Community

Number of Pages Required

4 page

Colors
9bcb3c
abd036
ffffff
f78f20
3176b5

Requirements
Must have
• Gallary
• moving gallary at the top
• About
• Testimonials
• Videos
• Leave a message

```html
<!DOCTYPE html>
<html lang="en">
<head>
<meta charset="utf-8">
<title>Halden Memorial</title>
<link href="https://fonts.googleapis.com/css2?family=Roboto:ital,wght@0,300;0,400;0,500;0,700;1,400&display=swap" rel="stylesheet">
<style>
:root{
  --blue:#3176b5;
  --navy:#1d3f7a;
  --green:#9bcb3c;
  --lime:#abd036;
  --orange:#f78f20;
  --orange-dark:#e0780f;
  --white:#ffffff;
  --page:#f2f2f2;
  --text:#6d6d6d;
  --line:#e2e2e2;
  --footer:#2b2b2b;
  --footer-bar:#1f1f1f;
  --footer-text:#a4a4a4;
}
*{box-sizing:border-box;margin:0;padding:0}
html,body{width:731px;height:1200px;overflow:hidden}
body{font-family:'Roboto',sans-serif;background:var(--page);position:relative;color:var(--text)}
.abs{position:absolute}
.masthead{left:0;top:0;width:731px;height:200px;background:linear-gradient(180deg,#1f4a8c,#1a3f7c);border-bottom:3px solid var(--green)}
.brand{left:60px;top:33px;font-size:19px;color:var(--white);font-weight:400;letter-spacing:.2px}
.brand b{color:var(--lime);font-weight:500}
.search{left:478px;top:31px;width:192px;height:25px;border:2px solid #c9d6e8;border-radius:3px;background:var(--white);display:flex}
.search span{flex:1;font-size:6.5px;color:#aaa;padding:8px 8px;font-style:italic}
.search i{width:30px;background:var(--green);display:flex;align-items:center;justify-content:center}
.sheet{left:60px;top:85px;width:611px;height:941px;background:var(--white)}
.nav{left:60px;top:85px;width:611px;height:33px;background:var(--lime);border-bottom:2px solid var(--orange);display:flex;align-items:center;justify-content:space-between;padding-right:24px}
.nav a{font-size:7px;color:var(--white);text-decoration:none;letter-spacing:.2px}
.nav a.active{background:var(--orange);height:33px;width:68px;display:flex;align-items:center;justify-content:center}
.hero-photo{left:60px;top:119px;width:418px;height:277px;background:linear-gradient(180deg,#b9c1bd 0%,#7c8a73 35%,#4f6a38 60%,#8a7f68 100%)}
.hero-panel{left:478px;top:119px;width:193px;height:277px;background:#262a26;text-align:center;color:var(--white)}
.hero-panel .kicker{margin-top:12px;font-size:11px;font-weight:700}
.hero-panel .name{font-size:15px;font-weight:300;margin-top:3px;letter-spacing:.3px}
.hero-panel .role{font-size:6px;margin-top:5px}
.hero-panel hr{border:0;border-top:1px solid #777;width:110px;margin:13px auto 0}
.meta{margin:12px 13px 0;height:22px;background:var(--green);display:flex;align-items:center;justify-content:center;gap:14px;font-size:6.5px;font-weight:500}
.meta span{display:flex;align-items:center;gap:3px}
.hero-panel p{font-size:6.5px;line-height:14px;margin:11px 10px 0}
.btn{background:linear-gradient(180deg,var(--orange),var(--orange-dark));color:var(--white);display:flex;align-items:center;justify-content:center;border-radius:2px}
.hero-btn{left:491px;top:353px;width:167px;height:28px;font-size:8px;font-weight:500}
h2{font-weight:400;color:var(--blue)}
.bio-title{left:74px;top:421px;font-size:16px}
.bio{left:74px;top:446px;width:380px}
.bio .lead{font-size:7.4px;line-height:14px;margin-bottom:8px}
.bio p{font-size:6.3px;line-height:14px;margin-bottom:8px}
.bio-btn{left:74px;top:611px;width:96px;height:29px;font-size:8px;font-weight:500}
.portrait{left:480px;top:424px;width:178px;height:216px;border:1px solid var(--line);padding:3px}
.portrait div{width:100%;height:100%;background:linear-gradient(160deg,#eef2f6,#c7d3df 60%,#2a2e38)}
.gal-title{left:74px;top:668px;font-size:11.5px}
.gal-rule{left:128px;top:675px;width:496px;border-top:1px solid var(--line)}
.arrows{left:628px;top:669px;display:flex;gap:3px}
.arrows span{width:13px;height:11px;background:#eee;font-size:7px;color:#999;display:flex;align-items:center;justify-content:center}
.shot{top:702px;width:190px;height:122px;border:1px solid var(--line)}
.shot.one{left:76px;background:var(--lime);opacity:.85;display:flex;align-items:center;justify-content:center;gap:10px}
.shot.one span{width:30px;height:30px;border-radius:50%;background:rgba(255,255,255,.35);display:flex;align-items:center;justify-content:center}
.shot.two{left:271px;background:linear-gradient(180deg,#c9c3bb,#e7e1d9)}
.shot.three{left:466px;background:linear-gradient(180deg,#d8cfc4,#b89c84)}
.test-title{left:74px;top:847px;font-size:11.5px}
.dots{left:640px;top:851px;display:flex;gap:2px}
.dots i{width:7px;height:7px;border-radius:50%;background:#ddd}
.quote{left:74px;top:875px;width:585px;font-size:6.6px;line-height:14px;font-style:italic;text-indent:17px}
.qmark{font-size:20px;color:#ccc;font-style:normal;font-family:Georgia,serif}
.q-open{left:73px;top:868px}
.q-close{left:386px;top:908px}
.test-rule{left:74px;top:940px;width:584px;border-top:1px solid var(--line)}
.avatar{left:75px;top:956px;width:49px;height:49px;border-radius:50%;background:linear-gradient(180deg,#d5dbe3,#53627a);border:2px solid #eee}
.cite{left:133px;top:976px;font-size:6.8px;color:var(--orange)}
.cite em{color:#bbb;font-size:6px}
.leave{left:511px;top:993px;width:160px;height:33px;background:var(--green);display:flex;align-items:center;padding-left:13px;gap:12px;color:var(--white);font-size:8.5px}
.leave .x{margin-left:auto;margin-right:9px;width:11px;height:11px;border-radius:50%;background:rgba(255,255,255,.45);font-size:7px;color:var(--green);display:flex;align-items:center;justify-content:center}
.footer{left:0;top:1026px;width:731px;height:144px;background:var(--footer)}
.fcol{top:1045px}
.fcol h3{font-size:8.3px;color:var(--white);font-weight:500;padding-bottom:8px;border-bottom:1px solid #444;margin-bottom:8px}
.fcol p{font-size:6.3px;line-height:13px;color:var(--footer-text)}
.fcol ul{list-style:none;font-size:6px;color:var(--footer-text)}
.fcol li{margin-bottom:8.6px;padding-left:9px;position:relative}
.fcol li:before{content:"";position:absolute;left:0;top:2px;width:3px;height:3px;border-radius:50%;background:#888}
.f-about{left:60px;width:135px}
.f-nav{left:235px;width:105px}
.f-nav .cols{display:flex;gap:18px}
.f-links{left:384px;width:98px}
.f-news{left:523px;width:148px}
.f-btn{width:49px;height:15px;font-size:6px;margin-top:10px}
.f-input{height:19px;background:var(--white);font-size:6px;color:#777;padding:6px 6px;margin-top:9px}
.f-sub{width:82px;height:22px;font-size:6.8px;margin-top:7px}
.bar{left:0;top:1170px;width:731px;height:30px;background:var(--footer-bar);display:flex;align-items:center;justify-content:space-between;padding:0 60px;font-size:6px;color:var(--white)}
.social{display:flex;align-items:center;gap:5px}
.social i{width:16px;height:16px;display:block}
</style>
</head>
<body>
<div class="abs masthead"></div>
<div class="abs brand"><b>HALDEN</b> MEMORIAL</div>
<div class="abs search"><span>Search...</span><i><svg width="8" height="8" viewBox="0 0 10 10"><circle cx="4" cy="4" r="3" fill="none" stroke="#fff" stroke-width="1.5"/><line x1="6.3" y1="6.3" x2="9" y2="9" stroke="#fff" stroke-width="1.5"/></svg></i></div>

<div class="abs sheet"></div>
<nav class="abs nav">
  <a class="active" href="#">HOME</a><a href="#">ABOUT US</a><a href="#">BIOGRAPHY</a><a href="#">SPEECHES</a><a href="#">VIDEOS</a><a href="#">GALLERY</a><a href="#">TESTIMONIALS</a><a href="#">CONTACT US</a>
</nav>

<div class="abs hero-photo" role="img" aria-label="Slideshow photo of a memorial garden with a grave stone, colonnade and red flowers"></div>
<div class="abs hero-panel">
  <div class="kicker">MY MOTHER'S</div>
  <div class="name">HALDEN MEMORIAL</div>
  <div class="role">SENIOR MEMBER OF THE LONDON COMMUNITY.</div>
  <hr>
  <div class="meta">
    <span><svg width="7" height="7" viewBox="0 0 10 10"><rect x="1" y="2" width="8" height="7" fill="none" stroke="#fff"/><line x1="1" y1="4" x2="9" y2="4" stroke="#fff"/></svg>OCTOBER 6TH 2015</span>
    <span><svg width="6" height="8" viewBox="0 0 8 10"><path d="M4 0C1.8 0 0 1.7 0 3.8 0 6.5 4 10 4 10s4-3.5 4-6.2C8 1.7 6.2 0 4 0z" fill="#fff"/><circle cx="4" cy="3.8" r="1.4" fill="#9bcb3c"/></svg>LONDON</span>
  </div>
  <p>Sed ut perspiciatis unde omnis iste natus error sit voluptatem accusantium doloremque laudantium, totam rem aperiam, eaque ipsa quae ab illo inventore veritatis et Nemo enim ipsam voluptatem quia voluptas sit aspernatur aut odit aut fugit, sed quia consequuntur magni dolor sit amet, consectetur, adipisci velit, sed quia non numquam eius modi tempora incidunt ...</p>
</div>
<div class="abs btn hero-btn">CLICK VIEW MORE ABOUT</div>

<h2 class="abs bio-title">BIOGRAPHY</h2>
<div class="abs bio">
  <p class="lead">Sed ut perspiciatis unde omnis iste natus error sit voluptatem accusantium doloremque laudantium, totam rem aperiam, eaque ipsa quae ab illo inventore veritatis et quasi architecto...</p>
  <p>Consequuntur magni dolores eos qui ratione voluptatem sequi nesciunt. Neque porro quisquam est, qui ipsum quia aliquam quaerat voluptatem. Ut enim ad minima veniam, quis nostrum exercitationem ullam corporis suscipit laboriosam, nisi ut aliquid ex ea commodi consequatur? Quis autem vel eum iure reprehenderit qui in ea voluptate velit esse quam nihil molestiae consequatur, vel illum qui dolorem eum fugiat quo ...</p>
  <p>Ipsum quia dolor sit amet, consectetur, adipisci velit, sed quia non numquam eius modi tempora incidunt ut labore et dolore magnam aliquam quaerat voluptatem. Ut enim ad minima veniam, quis nostrum exercitationem ullam corporis suscipit laboriosam, nisi ut aliquid ex ea commodi consequatur? Quis autem vel eum iure reprehenderit qui in ea voluptate velit esse quam nihil molestiae consequatur, vel illum qui dolorem eum fugiat quo...</p>
</div>
<div class="abs btn bio-btn">READ MORE BIO</div>
<div class="abs portrait"><div role="img" aria-label="Portrait photo of a man in a dark suit"></div></div>

<h2 class="abs gal-title">GALLERY</h2>
<div class="abs gal-rule"></div>
<div class="abs arrows"><span>&lsaquo;</span><span>&rsaquo;</span></div>
<div class="abs shot one" role="img" aria-label="Gallery photo of a smiling older woman, shown with hover overlay">
  <span><svg width="12" height="8" viewBox="0 0 12 8"><path d="M0 4C2 1 4 0 6 0s4 1 6 4c-2 3-4 4-6 4S2 7 0 4z" fill="#fff"/><circle cx="6" cy="4" r="1.8" fill="#abd036"/></svg></span>
  <span><svg width="10" height="10" viewBox="0 0 10 10"><rect x="0.5" y="4" width="5" height="3" rx="1.5" transform="rotate(-45 3 5.5)" fill="none" stroke="#fff" stroke-width="1.2"/><rect x="4.5" y="3" width="5" height="3" rx="1.5" transform="rotate(-45 7 4.5)" fill="none" stroke="#fff" stroke-width="1.2"/></svg></span>
</div>
<div class="abs shot two" role="img" aria-label="Gallery photo of an older woman with glasses"></div>
<div class="abs shot three" role="img" aria-label="Gallery photo of a woman resting her chin on her hands"></div>

<h2 class="abs test-title">TESTIMONIALS</h2>
<div class="abs dots"><i></i><i></i></div>
<span class="abs qmark q-open">&ldquo;</span>
<p class="abs quote">Neque porro quisquam est, qui dolorem ipsum quia dolor sit amet, consectetur,adipisci velit, sed quia non numquam eius modi tempora incidunt ut labore et dolore exercitationem ullam corporis suscipit laboriosam,sed do eiusmod tempor dolore magna aliqua. Ut enim ad minim veniam, quis nostrud exercitation ullamco laboris nisi ut aliquip ex ea commodo consequat. Duis aute irure dolo incididunt ut labore et dolore nisi ut aliquid ex ea ....</p>
<span class="abs qmark q-close">&rdquo;</span>
<div class="abs test-rule"></div>
<div class="abs avatar" role="img" aria-label="Photo of the person giving the testimonial"></div>
<div class="abs cite">-DANIEL HARTLEY <em>, Doloremque laudantium, totam</em></div>
<div class="abs leave">
  <svg width="22" height="16" viewBox="0 0 22 16"><path d="M1 7L21 1 15 15 10 10z" fill="#fff"/><path d="M10 10L21 1" stroke="#9bcb3c" stroke-width="1"/></svg>
  LEAVE A MESSAGE
  <span class="x">&times;</span>
</div>

<footer>
  <div class="abs footer"></div>
  <div class="abs fcol f-about">
    <h3>ABOUT HALDEN MEMORIAL</h3>
    <p>Sed ut perspiciatis unde omnis iste natus error sit voluptatem accusantium dolore itecto beatae vitae dicta sunt explicabo eius modi tempora incidunt....</p>
    <div class="btn f-btn">READ MORE</div>
  </div>
  <div class="abs fcol f-nav">
    <h3>NAVIGATION</h3>
    <div class="cols">
      <ul><li>HOME</li><li>ABOUT US</li><li>BIOGRAPHY</li><li>SPEECHES</li><li>VIDEOS</li></ul>
      <ul><li>TESTIMONIALS</li><li>CONTACT US</li></ul>
    </div>
  </div>
  <div class="abs fcol f-links">
    <h3>OTHER LINKS</h3>
    <ul><li>SUSPENDISSE LAOREET</li><li>DUIS IN AUGUE IN AUGUE</li><li>PELLENTESQUE FERMENTUM</li><li>ETIAM AC VELIT VITAE</li><li>NAM MAXIMUS NISI</li></ul>
  </div>
  <div class="abs fcol f-news">
    <h3>NEWS LETTER</h3>
    <p>SED UT PERSPICIATIS UNDE OMNIS ISTE NATUS VOLUPTATEM ACCUSANT DOLOREMQUE...</p>
    <div class="f-input">ENTER YOUR E-MAIL</div>
    <div class="btn f-sub">SUBSCRIBE</div>
  </div>
  <div class="abs bar">
    <span>COPYRIGHTS&copy;HALDEN MEMORIAL 2016 | ALLRIGHTS RESERVED.</span>
    <span class="social">CONNECT WITH US:
      <i style="background:#3b5a98"></i><i style="background:#2aa3df"></i><i style="background:#d34836"></i><i style="background:#c8232c"></i>
    </span>
  </div>
</footer>
</body>
</html>
```